Build a Web page - Dovin Pratchell Homes, LLC - a custom home builder

We are a custom home builder in Wisconsin. Need a basic web page with a home page, About Us, Contact info, Gallery, and Testimonials page. Gallery will probably have sub-pages and each will have about ten pictures or less. I already own the domain and have web hosting through Wix, I just need the site built. Once the page is built I should be able to do the upkeep on it myself. If I need to add pictures or whatever.
Updates

Project Deadline Extended
Reason: I am still looking through designs and will select soon - thank you!

Target Market(s)

Gen X and Millennials who are looking to build a home. Custom built homes - not generic spec homes.

Industry/Entity Type

Home Builder

Number of Pages Required

5+ page

Font styles to use
Sans Serif

Colors
ffffff
ec1f27
000000
9d9d9d

Requirements
Must have
• I have no idea if I want coded or in coded. I'm not sure of the difference and why I would want one over the other.
Nice to have
• We like the following colors - red, black, gray, white.
Should not have
• not a big fan of clip art like hammers, tape measures, etc. Must look professional.

```html
<!DOCTYPE html>
<html lang="en">
<head>
<meta charset="utf-8">
<title>Dovin Pratchell Homes</title>
<link href="https://fonts.googleapis.com/css2?family=Open+Sans:wght@400;600;700;800&display=swap" rel="stylesheet">
<style>
:root{
  --red:#ec1f27;
  --black:#000000;
  --ink:#333333;
  --gray:#9d9d9d;
  --muted:#8a8a8a;
  --white:#ffffff;
  --footer:#1c1c1c;
  --footer-deep:#111111;
}
*{box-sizing:border-box;margin:0;padding:0}
html,body{width:1200px;height:3358px;overflow:hidden}
body{position:relative;background:var(--white);font-family:"Open Sans",Arial,sans-serif;color:var(--ink)}
.abs{position:absolute}

/* Header + hero */
.hero{left:0;top:0;width:1200px;height:683px;overflow:hidden;
  background:linear-gradient(180deg,#6f8fb3 0%,#9fb4c6 22%,#5d6a56 45%,#4f5d43 70%,#5e7a3a 100%)}
.hero-shade{inset:0;background:rgba(0,0,0,.28)}
.hero-curve{left:0;top:0}
.topbar{right:38px;top:8px;font-size:13px;color:#666;display:flex;gap:26px;align-items:center}
.topbar span{display:flex;align-items:center;gap:7px}
.navbar{left:0;top:40px;width:1200px;height:50px;background:rgba(220,226,236,.82)}
.nav{right:0;top:40px;height:50px;display:flex;align-items:center}
.nav a{font-size:14px;font-weight:600;color:var(--black);text-decoration:none;margin-right:44px;text-transform:uppercase}
.nav a.active{color:var(--red)}
.nav a:last-child{margin-right:38px}
.logo-box{left:38px;top:22px;width:146px;height:158px;background:var(--white);box-shadow:0 2px 8px rgba(0,0,0,.25);
  display:flex;align-items:center;justify-content:center;text-align:center;padding:10px}
.logo-name{font-size:17px;font-weight:800;line-height:1.2;color:var(--black);text-transform:uppercase}
.hero-title{left:0;top:312px;width:1200px;text-align:center;color:var(--white);font-size:35px;font-weight:700;text-transform:uppercase;letter-spacing:.5px}
.hero-text{left:225px;top:372px;width:750px;text-align:center;color:var(--white);font-size:15px;line-height:22px}
.btn-read{left:527px;top:463px;width:146px;height:34px;border-radius:17px;background:var(--red);color:var(--white);
  font-size:12px;font-weight:600;display:flex;align-items:center;justify-content:center;gap:6px}
.hero-dots{left:566px;top:640px;display:flex;gap:10px}
.hero-dots i{width:14px;height:14px;border-radius:50%;border:2px solid var(--white);display:block}
.hero-dots i.on{border-color:var(--red)}

/* Feature tiles */
.features{left:38px;top:752px;width:1124px;height:238px;display:flex}
.feature{position:relative;flex:1;height:238px}
.feature-box{position:absolute;left:20px;right:20px;top:20px;bottom:20px;background:rgba(255,255,255,.88);
  display:flex;flex-direction:column;align-items:center;justify-content:center;text-align:center}
.feature-kicker{font-size:12px;font-weight:700;color:var(--black);text-transform:uppercase}
.feature-title{font-size:27px;font-weight:700;color:var(--black);text-transform:uppercase;line-height:1.2}
.feature-sub{font-size:12px;color:var(--gray)}

/* Section headings */
.section-title{left:0;width:1200px;text-align:center;font-size:23px;font-weight:700;color:#222;text-transform:uppercase;letter-spacing:.5px}
.section-title em{font-style:normal;color:var(--red)}
.divider{left:450px;width:300px;height:24px}

/* Welcome */
.welcome-copy{left:90px;top:1140px;width:783px;text-align:center;font-size:15px;line-height:26px;color:var(--gray)}
.welcome-copy p{margin-bottom:24px}
.welcome-badge{left:884px;top:1151px;width:260px;height:260px;border-radius:50%;background:var(--white);
  border:3px solid #ddd;box-shadow:0 0 0 6px #f1f1f1,0 2px 10px rgba(0,0,0,.2);
  display:flex;align-items:center;justify-content:center;text-align:center}
.welcome-badge .logo-name{font-size:22px}

/* Gallery */
.gallery{left:38px;top:1603px;width:1124px;height:614px;display:grid;
  grid-template-columns:repeat(4,281px);grid-template-rows:repeat(4,153.5px)}
.g{position:relative}
.g-big{grid-column:1/3;grid-row:1/3}
.g-tall{grid-row:3/5}
.g-frame{position:absolute;left:20px;top:20px;right:20px;bottom:20px;border:2px solid rgba(255,255,255,.9)}
.g-label{position:absolute;left:30px;right:30px;top:130px;height:40px;background:rgba(0,0,0,.72);color:var(--white);
  font-size:16px;font-weight:600;display:flex;align-items:center;justify-content:center;text-transform:uppercase}

/* Testimonials */
.testimonials{left:0;top:2380px;width:1200px;height:390px;
  background:linear-gradient(90deg,#3a2a20 0%,#6b5a48 35%,#8e8574 60%,#5c4a3a 100%)}
.testimonials-shade{inset:0;background:rgba(0,0,0,.45)}
.quote-mark{left:0;top:2420px;width:1200px;text-align:center;color:var(--white);font-size:54px;font-weight:800;line-height:1}
.quote-text{left:110px;top:2499px;width:980px;text-align:center;color:var(--white);font-size:15px;line-height:24px}
.quote-name{left:0;top:2641px;width:1200px;text-align:center;color:var(--red);font-size:15px;font-weight:700}
.quote-rule{left:582px;top:2672px;width:36px;height:2px;background:var(--white)}
.quote-dots{left:535px;top:2714px;display:flex;gap:12px}
.quote-dots i{display:block;width:36px;height:5px;background:var(--white)}
.quote-dots i.on{background:var(--red)}

/* Newsletter */
.newsletter{left:38px;top:2826px;width:1124px;height:174px;background:var(--red);overflow:hidden}
.newsletter-photo{left:0;top:0}
.news-title{left:593px;top:2862px;color:var(--white);font-size:20px;font-weight:700;text-transform:uppercase}
.news-text{left:593px;top:2892px;width:500px;color:var(--white);font-size:12px;line-height:19px}
.news-form{left:593px;top:2949px;width:572px;height:44px;border:2px solid var(--white);border-radius:22px;display:flex;align-items:center;justify-content:space-between}
.news-form span{color:var(--white);font-size:14px;padding-left:28px}
.news-form b{height:40px;width:118px;border-radius:20px;background:var(--white);color:var(--red);font-size:14px;font-weight:700;display:flex;align-items:center;justify-content:center;text-transform:uppercase}

/* Footer */
.footer{left:0;top:3054px;width:1200px;height:304px;background:var(--footer)}
.footer-bottom{left:0;top:3309px;width:1200px;height:49px;background:var(--footer-deep);border-top:1px solid #333;
  color:#bbb;font-size:12px;display:flex;align-items:center;justify-content:center}
.footer-bottom em{font-style:normal;color:var(--red)}
.f-head{color:var(--white);font-size:16px;font-weight:700}
.f-head::after{content:"";display:block;width:38px;height:3px;background:var(--red);margin-top:9px}
.f-links{display:grid;grid-template-columns:170px 170px;row-gap:10px}
.f-links span,.f-contact span,.f-hours span{color:#ddd;font-size:13px}
.f-links span{display:flex;align-items:center;gap:8px}
.f-contact{display:flex;flex-direction:column;gap:14px}
.f-contact div{display:flex;gap:14px;align-items:flex-start}
.f-contact span{line-height:19px}
.f-hours{display:grid;grid-template-columns:105px 120px;row-gap:8px}
.social{display:flex;gap:12px}
.social i{display:block;width:36px;height:36px;border:1px solid #ccc}
</style>
</head>
<body>

<!-- Hero -->
<div class="abs hero" role="img" aria-label="Photo of a two-storey green-sided custom home with a lawn under a blue sky"></div>
<div class="abs hero-shade" style="left:0;top:0;width:1200px;height:683px"></div>
<svg class="abs hero-curve" width="1200" height="684" viewBox="0 0 1200 684">
  <path d="M0 598 Q600 760 1200 598 L1200 684 L0 684 Z" fill="#ffffff"/>
</svg>

<div class="abs navbar"></div>
<div class="abs topbar" style="z-index:2">
  <span><svg width="12" height="12" viewBox="0 0 24 24"><path d="M6.6 10.8a15 15 0 0 0 6.6 6.6l2.2-2.2c.3-.3.7-.4 1-.2 1.1.4 2.3.6 3.6.6.6 0 1 .4 1 1V20c0 .6-.4 1-1 1C10.6 21 3 13.4 3 4c0-.6.4-1 1-1h3.5c.6 0 1 .4 1 1 0 1.3.2 2.5.6 3.6.1.3 0 .7-.2 1z" fill="#666"/></svg>+123 555 0190</span>
  <span><svg width="13" height="11" viewBox="0 0 26 20"><rect x="1" y="1" width="24" height="18" fill="none" stroke="#666" stroke-width="2"/><path d="M1 1 L13 11 L25 1" fill="none" stroke="#666" stroke-width="2"/></svg>info@dovinpratchellhomes.com</span>
</div>
<nav class="abs nav">
  <a class="active">Home</a><a>About Us</a><a>Gallery</a><a>Testimonials</a><a>Contact Us</a>
</nav>
<div class="abs logo-box"><span class="logo-name">Dovin Pratchell Homes</span></div>

<h1 class="abs hero-title">Lorem ipsum dolor sit amet...</h1>
<p class="abs hero-text">Lorem Ipsum is simply dummy text of the printing and typesetting industry. Lorem Ipsum has been the industry's standard dummy text ever since the 1500s, when an unknown printer took a galley of type and scrambled it to make a type specimen book.</p>
<div class="abs btn-read">READ MORE <svg width="14" height="10" viewBox="0 0 14 10"><path d="M0 5h11M8 1l4 4-4 4" stroke="#fff" stroke-width="2" fill="none"/></svg></div>
<div class="abs hero-dots"><i></i><i class="on"></i><i></i></div>

<!-- Feature tiles -->
<section class="abs features">
  <div class="feature" role="img" aria-label="Photo of a new home exterior with a porch railing" style="background:linear-gradient(135deg,#6f8a4a,#b9b5a6 60%,#8a7a66)">
    <div class="feature-box"><span class="feature-kicker">Get the new look</span><span class="feature-title">New Design</span><span class="feature-sub">Furniture Collection</span></div>
  </div>
  <div class="feature" role="img" aria-label="Photo of a warm lit living room interior" style="background:linear-gradient(135deg,#6a4a30,#b59670 55%,#4a3322)">
    <div class="feature-box"><span class="feature-kicker">Get the new look</span><span class="feature-title">New Home Design</span><span class="feature-sub">Furniture Collection</span></div>
  </div>
  <div class="feature" role="img" aria-label="Photo of a bright white kitchen interior" style="background:linear-gradient(135deg,#c9c4bb,#e9e6e1 55%,#8f8a82)">
    <div class="feature-box"><span class="feature-kicker">Get the new look</span><span class="feature-title">New Design</span><span class="feature-sub">Furniture Collection</span></div>
  </div>
</section>

<!-- Welcome -->
<h2 class="abs section-title" style="top:1046px">Welcome to <em>Dovin Pratchell Homes</em></h2>
<svg class="abs divider" style="top:1088px" viewBox="0 0 300 24"><line x1="0" y1="12" x2="126" y2="12" stroke="#bbb"/><line x1="174" y1="12" x2="300" y2="12" stroke="#bbb"/><rect x="141" y="3" width="18" height="18" transform="rotate(45 150 12)" fill="none" stroke="#ec1f27" stroke-width="2"/><rect x="146" y="8" width="8" height="8" transform="rotate(45 150 12)" fill="#ec1f27"/></svg>
<div class="abs welcome-copy">
  <p>Lorem Ipsum is simply dummy text of the printing and typesetting industry. Lorem Ipsum has been the industry's standard dummy text ever since the 1500s, when an unknown printer took a galley of type and scrambled it to make a type specimen book. It has survived not only five centuries, but also the leap into electronic typesetting, remaining essentially unchanged.</p>
  <p>It was popularised in the 1960s with the release of Letraset sheets containing Lorem Ipsum passages, and more recently with desktop publishing software like Aldus PageMaker including versions of Lorem Ipsum.</p>
  <p>Ut enim ad minim veniam, quis nostrud exercitation ullamco laboris nisi ut aliquip ex ea commodo consequat. Duis aute irure dolor in reprehenderit in voluptate velit esse cillum dolore eu fugiat nulla pariatur.</p>
</div>
<div class="abs welcome-badge"><span class="logo-name">Dovin<br>Pratchell<br>Homes</span></div>

<!-- Gallery -->
<h2 class="abs section-title" style="top:1500px">Our <em>Gallery</em></h2>
<svg class="abs divider" style="top:1542px" viewBox="0 0 300 24"><line x1="0" y1="12" x2="126" y2="12" stroke="#bbb"/><line x1="174" y1="12" x2="300" y2="12" stroke="#bbb"/><rect x="141" y="3" width="18" height="18" transform="rotate(45 150 12)" fill="none" stroke="#ec1f27" stroke-width="2"/><rect x="146" y="8" width="8" height="8" transform="rotate(45 150 12)" fill="#ec1f27"/></svg>
<section class="abs gallery">
  <div class="g g-big" role="img" aria-label="Photo of a living room with red armchairs and a fireplace" style="background:linear-gradient(135deg,#c9b79a,#8c5a44 55%,#5e3a2c)">
    <div class="g-frame"></div><div class="g-label">New Home Design</div>
  </div>
  <div class="g" role="img" aria-label="Photo of a family room with a leather sectional" style="background:linear-gradient(135deg,#b8a88e,#6e5442)"></div>
  <div class="g" role="img" aria-label="Photo of a living room with a stone fireplace" style="background:linear-gradient(135deg,#a08a70,#d8cbb6)"></div>
  <div class="g" role="img" aria-label="Photo of a two-storey home exterior" style="background:linear-gradient(180deg,#aebfd2,#c9c4ba 50%,#6d7a4a)"></div>
  <div class="g" role="img" aria-label="Photo of a wooden back deck" style="background:linear-gradient(180deg,#c8cbc2,#8a4a3a 65%,#6a7a48)"></div>
  <div class="g" role="img" aria-label="Photo of a bathroom vanity" style="background:linear-gradient(135deg,#d7cfa4,#8b6a4a)"></div>
  <div class="g" role="img" aria-label="Photo of a single-storey home exterior with lawn" style="background:linear-gradient(180deg,#cfd7df,#a99a86 50%,#5f8a3a)"></div>
  <div class="g g-tall" role="img" aria-label="Photo of a kitchen with wood cabinets and island" style="background:linear-gradient(180deg,#d9c8ae,#8a5a32 55%,#3a3a36)"></div>
  <div class="g g-tall" role="img" aria-label="Photo of an open dining and living area" style="background:linear-gradient(180deg,#e3e1dc,#9a948a 55%,#4a3a36)"></div>
  <div class="g" role="img" aria-label="Photo of a white bathroom" style="background:linear-gradient(135deg,#e9e9e6,#b5b3ac)"></div>
  <div class="g" role="img" aria-label="Photo of a green-sided home exterior" style="background:linear-gradient(180deg,#9fb7d4,#5e6e4a 55%,#6a9a3a)"></div>
</section>

<!-- Testimonials -->
<h2 class="abs section-title" style="top:2280px;font-size:22px">Testimonials</h2>
<svg class="abs divider" style="top:2321px" viewBox="0 0 300 24"><line x1="0" y1="12" x2="126" y2="12" stroke="#bbb"/><line x1="174" y1="12" x2="300" y2="12" stroke="#bbb"/><rect x="141" y="3" width="18" height="18" transform="rotate(45 150 12)" fill="none" stroke="#ec1f27" stroke-width="2"/><rect x="146" y="8" width="8" height="8" transform="rotate(45 150 12)" fill="#ec1f27"/></svg>
<section class="abs testimonials" role="img" aria-label="Photo of a living room with a stone fireplace and wood shelving"></section>
<div class="abs testimonials-shade" style="left:0;top:2380px;width:1200px;height:390px"></div>
<div class="abs quote-mark">“</div>
<p class="abs quote-text">Lorem ipsum dolor sit amet, consectetur adipiscing elit, sed do eiusmod tempor incididunt ut labore et dolore magna aliqua. Ut enim ad minim veniam, quis nostrud exercitation ullamco laboris nisi ut aliquip ex ea commodo consequat. Duis aute irure dolor in reprehenderit in voluptate velit esse cillum dolore eu fugiat nulla pariatur. Excepteur sint occaecat cupidatat non proident, sunt in culpa qui officia deserunt mollit anim id est laborum.</p>
<div class="abs quote-name">Nolan Avery</div>
<div class="abs quote-rule"></div>
<div class="abs quote-dots"><i></i><i class="on"></i><i></i></div>

<!-- Newsletter -->
<section class="abs newsletter">
  <svg class="abs newsletter-photo" width="575" height="174" viewBox="0 0 575 174">
    <defs><linearGradient id="nlPhoto" x1="0" y1="0" x2="1" y2="1"><stop offset="0" stop-color="#c9a46a"/><stop offset=".5" stop-color="#8a5a3a"/><stop offset="1" stop-color="#4a3024"/></linearGradient></defs>
    <path d="M0 0 H572 L404 174 H0 Z" fill="url(#nlPhoto)" role="img" aria-label="Photo of a cozy living room with a lamp and armchair"/>
  </svg>
</section>
<div class="abs news-title">Subscribe to our newsletter</div>
<p class="abs news-text">Lorem ipsum dolor sit amet, consectetur adipiscing elit, sed do eiusmod tempor incididunt...</p>
<div class="abs news-form"><span>Your Email</span><b>Subscribe!</b></div>

<!-- Footer -->
<footer class="abs footer"></footer>
<div class="abs" style="left:38px;top:3086px">
  <div class="f-head">Menu Link</div>
  <div class="f-links" style="margin-top:26px">
    <span>→ Home</span><span>→ About Us</span>
    <span>→ Gallery</span><span>→ Testimonials</span>
    <span>→ Contact Us</span><span>→ Term and condition</span>
    <span>→ Privacy Policy</span>
  </div>
</div>
<div class="abs" style="left:524px;top:3086px">
  <div class="f-head">Contact Information</div>
  <div class="f-contact" style="margin-top:26px">
    <div><svg width="14" height="18" viewBox="0 0 14 18"><path d="M7 0a7 7 0 0 0-7 7c0 5 7 11 7 11s7-6 7-11a7 7 0 0 0-7-7zm0 9.5A2.5 2.5 0 1 1 7 4.5a2.5 2.5 0 0 1 0 5z" fill="#fff"/></svg><span>27, Birchwood Lane<br>54321, Lakeview, Ipsum.</span></div>
    <div><svg width="14" height="14" viewBox="0 0 24 24"><path d="M6.6 10.8a15 15 0 0 0 6.6 6.6l2.2-2.2c.3-.3.7-.4 1-.2 1.1.4 2.3.6 3.6.6.6 0 1 .4 1 1V20c0 .6-.4 1-1 1C10.6 21 3 13.4 3 4c0-.6.4-1 1-1h3.5c.6 0 1 .4 1 1 0 1.3.2 2.5.6 3.6.1.3 0 .7-.2 1z" fill="#fff"/></svg><span>+123 555 0190</span></div>
    <div><svg width="14" height="14" viewBox="0 0 14 14"><rect x="0" y="5" width="14" height="9" fill="#fff"/><rect x="3" y="0" width="8" height="5" fill="none" stroke="#fff" stroke-width="1.5"/><rect x="3" y="8" width="8" height="2" fill="#1c1c1c"/></svg><span>+123 555 0199</span></div>
    <div><svg width="15" height="12" viewBox="0 0 26 20"><rect x="1" y="1" width="24" height="18" fill="none" stroke="#fff" stroke-width="2"/><path d="M1 1 L13 11 L25 1" fill="none" stroke="#fff" stroke-width="2"/></svg><span>info@dovinpratchellhomes.com</span></div>
  </div>
</div>
<div class="abs" style="left:873px;top:3086px">
  <div class="f-head">Opening Hours</div>
  <div class="f-hours" style="margin-top:26px">
    <span>Mon to Sat</span><span>09:00 to 09:00</span>
    <span>Sunday</span><span>Closed</span>
  </div>
  <div class="social" style="margin-top:42px"><i></i><i></i><i></i><i></i></div>
</div>
<div class="abs footer-bottom">Copyright © 2017&nbsp;<em>dovinpratchellhomes.com</em>. All Rights Reserved.</div>

</body>
</html>
```